LED strip light bag design

We are brivane lighting, a LED strip manufacturer in China, We need a packaging design for our LED strip light, as the strip market is full of standard package, so we want to make our package special, and use color orange, black and grey

Target Market(s)

USA, Europe

Contact Information for Business Card

Colin Wu
Director
Shenzhen Brivane Lighting Co., Ltd.
Add: 3F, Haodong Ind. Zone, Wenpu Rd, Baiqiao, Shenzhen 518420 China
Tel: +86-139-4826 3074 Fax: +86-755-28394610
E-mail: colin.wu@brivane-example.com

Font styles to use
Sans Serif
Other font styles liked:
• Tw Cen MT Condensed

Colors

Designer to choose only greyscale colors for use in the design.

Requirements
Must have
• Must have instructions of how to use the strip and CAUTION
• Must have CE, RoHS UL, trash can, ISO9001 logo
Nice to have
• Nice to have a back ground pictures with a strip drawing.

```html
<!DOCTYPE html>
<html lang="en">
<head>
<meta charset="utf-8">
<title>Brivane LED Strip Light Bag</title>
<link rel="stylesheet" href="https://fonts.googleapis.com/css2?family=Saira+Semi+Condensed:wght@400;500&family=Saira+Extra+Condensed:wght@400;500&display=swap">
<style>
  :root {
    --paper: #ffffff;
    --charcoal: #2b2b2d;
    --orange: #f36f21;
    --sun-core: #ffd200;
    --white: #ffffff;
    --fold: #3a3a3c;
  }
  * { margin: 0; padding: 0; box-sizing: border-box; }
  html, body {
    width: 1200px; height: 686px; overflow: hidden;
    background: var(--paper);
  }
  .bag {
    position: relative; width: 1200px; height: 686px;
    font-family: "Saira Extra Condensed", "Arial Narrow", sans-serif;
    color: var(--white);
  }
  .artwork { position: absolute; inset: 0; }
  .brand {
    position: absolute; top: 130px;
    display: flex; align-items: center; gap: 8px;
    font-family: "Saira Semi Condensed", "Arial Narrow", sans-serif;
    font-weight: 500; font-size: 30px; line-height: 36px; letter-spacing: 1px;
    white-space: nowrap; color: var(--white);
  }
  .brand-dot {
    width: 26px; height: 26px; border-radius: 50%;
    background: var(--orange);
  }
  .brand--front { left: 383px; }
  .brand--back { left: 630px; }
  .band-title {
    position: absolute;
    font-family: "Saira Semi Condensed", "Arial Narrow", sans-serif;
    font-size: 56px; font-weight: 400; line-height: 1;
    white-space: nowrap; color: var(--white);
    transform-origin: center center;
    text-shadow: 2px 2px 3px rgba(0,0,0,0.35);
  }
  .band-title--front { left: 242px; top: 420px; transform: translate(-50%, -50%) rotate(-59.7deg); }
  .band-title--back { left: 958px; top: 420px; transform: translate(-50%, -50%) rotate(59.7deg); }
  .headline {
    position: absolute; left: 344px; width: 240px; top: 376px;
    text-align: center; font-size: 24px; line-height: 36px; letter-spacing: 0.5px;
    white-space: nowrap;
  }
  .headline-line { display: block; }
  .headline-rule {
    position: absolute; left: 383px; top: 452px; width: 163px; height: 3px;
    background: var(--orange);
  }
  .headline-sub {
    position: absolute; left: 344px; width: 240px; top: 466px;
    text-align: center; font-size: 16px; line-height: 22px; letter-spacing: 0.5px;
    white-space: nowrap;
  }
  .caution {
    position: absolute; left: 649px; top: 392px; width: 211px; height: 186px;
    border: 1.5px solid var(--white); border-radius: 14px;
    padding: 5px 9px; font-size: 8px; line-height: 10px;
    overflow: hidden;
  }
  .caution-title { text-align: center; font-size: 14px; line-height: 16px; }
  .caution-lead { text-align: center; font-size: 8.5px; line-height: 11px; margin-bottom: 8px; }
  .caution-list { list-style: none; }
  .caution-list li { padding-left: 8px; text-indent: -8px; }
  .cert-row {
    position: absolute; left: 655px; top: 601px;
    display: flex; align-items: center; gap: 10px;
  }
  .cert { background: var(--white); }
  .cert--round { width: 30px; height: 30px; border-radius: 50%; }
  .cert--square { width: 30px; height: 30px; }
  .cert--wide { width: 60px; height: 26px; }
</style>
</head>
<body>
<div class="bag">
  <svg class="artwork" width="1200" height="686" viewBox="0 0 1200 686" xmlns="http://www.w3.org/2000/svg">
    <defs>
      <radialGradient id="sunLeft" cx="152" cy="290" r="300" gradientUnits="userSpaceOnUse">
        <stop offset="0" stop-color="#ffd200"/>
        <stop offset="0.55" stop-color="#f89a1c"/>
        <stop offset="1" stop-color="#f36f21"/>
      </radialGradient>
      <radialGradient id="sunRight" cx="1048" cy="290" r="300" gradientUnits="userSpaceOnUse">
        <stop offset="0" stop-color="#ffd200"/>
        <stop offset="0.55" stop-color="#f89a1c"/>
        <stop offset="1" stop-color="#f36f21"/>
      </radialGradient>
      <radialGradient id="haze" cx="0.5" cy="0.5" r="0.5">
        <stop offset="0" stop-color="#555558" stop-opacity="0.55"/>
        <stop offset="1" stop-color="#555558" stop-opacity="0"/>
      </radialGradient>
      <clipPath id="panel"><rect x="20" y="20" width="1160" height="646"/></clipPath>
      <filter id="lift" x="-10%" y="-10%" width="120%" height="120%">
        <feDropShadow dx="0" dy="3" stdDeviation="3" flood-color="#000" flood-opacity="0.45"/>
      </filter>
    </defs>
    <rect x="20" y="20" width="1160" height="646" fill="var(--charcoal)"/>
    <g clip-path="url(#panel)">
      <g role="img" aria-label="Grey halftone dot wave texture">
        <ellipse cx="110" cy="440" rx="150" ry="150" fill="url(#haze)"/>
        <ellipse cx="440" cy="560" rx="180" ry="80" fill="url(#haze)"/>
        <ellipse cx="1090" cy="440" rx="150" ry="150" fill="url(#haze)"/>
      </g>
      <polygon role="img" aria-label="Orange sunburst rays" points="20,20 325,20 160,296 144,300 20,232" fill="url(#sunLeft)"/>
      <polygon role="img" aria-label="Orange sunburst rays" points="1180,20 875,20 1040,296 1056,300 1180,232" fill="url(#sunRight)"/>
      <g filter="url(#lift)" fill="none" stroke="var(--orange)" stroke-linejoin="round">
        <polyline points="360,192 600,330 840,192" stroke-width="30"/>
        <line x1="76" y1="700" x2="368" y2="200" stroke-width="62" stroke-linecap="round"/>
        <line x1="1124" y1="700" x2="832" y2="200" stroke-width="62" stroke-linecap="round"/>
      </g>
    </g>
    <line x1="600" y1="20" x2="600" y2="666" stroke="var(--fold)" stroke-width="1"/>
  </svg>

  <div class="brand brand--front"><span class="brand-dot"></span>BRIVANE</div>
  <div class="brand brand--back"><span class="brand-dot"></span>BRIVANE</div>

  <div class="band-title band-title--front">LED STRIP LIGHT</div>
  <div class="band-title band-title--back">LED STRIP LIGHT</div>

  <div class="headline">
    <span class="headline-line">EASY TO USE LED</span>
    <span class="headline-line">STRIP LIGHTNING</span>
  </div>
  <div class="headline-rule"></div>
  <div class="headline-sub">INSTRUCTIONS</div>

  <div class="caution">
    <div class="caution-title">CAUTION</div>
    <div class="caution-lead">THIS BAG CONTAINS MOISTURE<br>AND ELECTROSTATIC SENSITIVE DEVICES.</div>
    <div>Attention</div>
    <ol class="caution-list">
      <li>1. Stroage Temperature:- 40 + 80°C<br>&nbsp;&nbsp;Operating Temperature:- 25 + 60°C</li>
      <li>2. Installation surface must be smooth, clean and dry.</li>
      <li>3. The part of LED components can not be fixed on the surface of the sharp edge.</li>
      <li>4. Strip should not be collided or crushed.</li>
      <li>5. Strip can be cut following the cutting lines.</li>
      <li>6. The led strips, must not exceed 5 meters, when used in a DC series circuit.</li>
    </ol>
  </div>

  <div class="cert-row">
    <span class="cert cert--square" aria-label="Certification mark"></span>
    <span class="cert cert--wide" aria-label="Certification mark"></span>
    <span class="cert cert--round" aria-label="Certification mark"></span>
    <span class="cert cert--square" aria-label="Disposal mark"></span>
    <span class="cert cert--round" aria-label="Certification mark"></span>
    <span class="cert cert--wide" aria-label="Quality certification mark"></span>
  </div>
</div>
</body>
</html>
```